Redesign of Bright Harbor Entertainment Card

I already have my logo and font design for my company name. I am looking to come up with a Unique way of having it on my business card. Just looking for a really hip, and professional business card while still using my logo design.

I have also enclosed the front and back of the card so you can see what I have now. Looking for something different.

Thank you!

Target Market(s)

Young to middle aged brides and grooms

Industry/Entity Type

Business

Requirements
Should not have
• Cheese

```html
<!DOCTYPE html>
<html lang="en">
<head>
<meta charset="utf-8">
<title>Bright Harbor Entertainment – Business Card</title>
<link href="https://fonts.googleapis.com/css2?family=Raleway:wght@300;400;500&display=swap" rel="stylesheet">
<style>
  :root {
    --bg: #e9eaec;
    --card: #ffffff;
    --brand-blue: #1a93d1;
    --ink-navy: #2d2a7c;
    --ink-grey: #8f8f98;
    --ink-light: #ffffff;
    --wash: #e6e6f2;
  }
  * { box-sizing: border-box; margin: 0; padding: 0; }
  html, body { width: 1200px; height: 873px; overflow: hidden; }
  body {
    background: var(--bg);
    font-family: "Raleway", sans-serif;
    position: relative;
  }
  .card {
    position: absolute;
    top: 282px;
    width: 540px;
    height: 309px;
    background: var(--card);
    overflow: hidden;
    box-shadow: 0 2px 8px rgba(0,0,0,.12);
  }
  .card--front { left: 40px; }
  .card--back { left: 620px; }

  /* front */
  .front-wash {
    position: absolute;
    left: -30px; top: 40px;
    width: 230px; height: 230px;
    border-radius: 50%;
    background: var(--wash);
    opacity: .7;
  }
  .front-subtitle {
    position: absolute;
    left: 40px; top: 34px;
    font-size: 12px;
    font-weight: 400;
    letter-spacing: .12em;
    text-transform: uppercase;
    color: var(--ink-grey);
  }
  .front-name {
    position: absolute;
    left: 36px; top: 52px;
    font-size: 62px;
    font-weight: 300;
    letter-spacing: .04em;
    text-transform: uppercase;
    color: var(--ink-navy);
    line-height: 1.1;
  }
  .contact-band {
    position: absolute;
    left: 0; right: 0;
    top: 170px; height: 96px;
    background: var(--brand-blue);
    display: flex;
    justify-content: space-around;
    align-items: center;
    padding: 0 20px;
  }
  .contact-item {
    display: flex;
    flex-direction: column;
    align-items: center;
    gap: 8px;
    width: 150px;
  }
  .contact-icon {
    width: 38px; height: 38px;
    border: 2px dashed var(--ink-light);
    border-radius: 50%;
    display: flex; align-items: center; justify-content: center;
  }
  .contact-icon--plain { border-style: solid; }
  .contact-label {
    font-size: 10px;
    letter-spacing: .06em;
    text-transform: uppercase;
    color: var(--ink-light);
    text-align: center;
    line-height: 1.3;
  }

  /* back */
  .back-band {
    position: absolute;
    left: 0; right: 0;
    background: var(--brand-blue);
  }
  .back-band--top { top: 0; height: 66px; }
  .back-band--bottom { bottom: 0; height: 80px; }
  .brand-lockup {
    position: absolute;
    left: 0; right: 0;
    top: 66px; height: 163px;
    display: flex;
    align-items: center;
    justify-content: center;
    gap: 16px;
  }
  .brand-mark {
    width: 58px; height: 58px;
    border-radius: 50%;
    background: var(--brand-blue);
    flex: none;
  }
  .brand-text { display: flex; flex-direction: column; }
  .brand-name {
    font-size: 40px;
    font-weight: 500;
    letter-spacing: .1em;
    text-transform: uppercase;
    color: var(--ink-navy);
    line-height: 1;
  }
  .brand-tagline {
    margin-top: 8px;
    font-size: 11px;
    letter-spacing: .14em;
    text-transform: uppercase;
    color: var(--brand-blue);
  }
</style>
</head>
<body>

  <section class="card card--front">
    <div class="front-wash"></div>
    <p class="front-subtitle">Bright Harbor Entertainment &amp; Event Professional</p>
    <h1 class="front-name">Evan Carter</h1>
    <div class="contact-band">
      <div class="contact-item">
        <span class="contact-icon contact-icon--plain"></span>
        <span class="contact-label">Bright Harbor<br>Entertainment</span>
      </div>
      <div class="contact-item">
        <span class="contact-icon">
          <svg width="18" height="18" viewBox="0 0 24 24" fill="#ffffff" aria-hidden="true">
            <path d="M6.6 10.8c1.4 2.8 3.8 5.1 6.6 6.6l2.2-2.2c.3-.3.7-.4 1-.2 1.1.4 2.3.6 3.6.6.6 0 1 .4 1 1V20c0 .6-.4 1-1 1C10.6 21 3 13.4 3 4c0-.6.4-1 1-1h3.5c.6 0 1 .4 1 1 0 1.3.2 2.5.6 3.6.1.3 0 .7-.2 1L6.6 10.8z"/>
          </svg>
        </span>
        <span class="contact-label">(555) 014-2270 (4100)</span>
      </div>
      <div class="contact-item">
        <span class="contact-icon">
          <svg width="20" height="20" viewBox="0 0 24 24" fill="none" stroke="#ffffff" stroke-width="1.6" aria-hidden="true">
            <circle cx="12" cy="12" r="9"/>
            <ellipse cx="12" cy="12" rx="4" ry="9"/>
            <line x1="3" y1="12" x2="21" y2="12"/>
            <line x1="5" y1="7" x2="19" y2="7"/>
            <line x1="5" y1="17" x2="19" y2="17"/>
          </svg>
        </span>
        <span class="contact-label">brightharbor.com</span>
      </div>
    </div>
  </section>

  <section class="card card--back">
    <div class="back-band back-band--top"></div>
    <div class="brand-lockup">
      <span class="brand-mark"></span>
      <div class="brand-text">
        <span class="brand-name">Bright Harbor</span>
        <span class="brand-tagline">Entertainment &amp; Event Professionals</span>
      </div>
    </div>
    <div class="back-band back-band--bottom"></div>
  </section>

</body>
</html>
```